Stationery Design Project for High End Wealth Management Firm

We need a stationery design for our high-end wealth management firm. Our clientele are affluent and our brand is built around providing investment services with world-class service.

The final concepts should provide a business card, letterhead, and envelope.

We like the idea of having text on the front and back and we MUST have black front and back business cards.
For the business card we have the following that needs to be included:
Company Logo & Tagline
Employee Name
Employee title
Employee Email
Website
2 seperate office cities, addresses, and phone numbers
Financial disclosure (small print)

Having black envelopes would be neat, but black is not a must for the envelopes.
Updates

Project Deadline Extended
Reason: To give the concept one more day of revisions.

Project Deadline Extended
Reason: To allow for more concepts and designs.

Target Market(s)

High Net Worth

Industry/Entity Type

Business

Requirements
Must have
• The following disclosure must be on the back of the card in small print:

Investment Advisory Services offered through Harrowgate Asset Partners LLC, a SEC Registered Investment Advisor. Corvane Wealth Management LLC is not affiliated with Harrowgate Asset Partners LLC.

Black business cards are also a must have.

Please utilize each of the 3 components of our logo in the design.

Please use our white background logo elements when designing our letterhead if you need them.
Nice to have
• Please use our company colors when designing. Utilize a combination of the elements of our logo that we have attached.

We are going to be printing our business cards on letterpress.

```html
<!DOCTYPE html>
<html lang="en">
<head>
<meta charset="utf-8">
<title>Corvane Wealth Management — Stationery</title>
<link rel="stylesheet" href="https://fonts.googleapis.com/css2?family=Cormorant+Garamond:wght@400;500;600&family=Playfair+Display:ital,wght@1,700&display=swap">
<style>
  :root {
    --page: #ffffff;
    --sheet: #231f20;
    --sheet-edge: #3a3536;
    --gold: #c8912e;
    --gold-light: #f0c56a;
    --silver: #d9d9d9;
    --ink: #ffffff;
    --ink-soft: #bdb8b4;
  }
  * { box-sizing: border-box; margin: 0; padding: 0; }
  html, body { width: 1200px; height: 868px; overflow: hidden; background: var(--page); }
  .stationery { position: relative; width: 1200px; height: 868px; font-family: "Cormorant Garamond", Georgia, serif; color: var(--ink); }
  .piece { position: absolute; background: var(--sheet); border: 1px solid var(--sheet-edge); overflow: hidden; }

  .envelope { left: 16px; top: 16px; width: 520px; height: 252px; }
  .card-contact { left: 58px; top: 301px; width: 474px; height: 260px; }
  .card-brand { left: 58px; top: 581px; width: 474px; height: 239px; }
  .letterhead { left: 583px; top: 8px; width: 604px; height: 800px; }

  .wordmark { position: absolute; z-index: 1; font-weight: 500; color: var(--silver); line-height: 1; letter-spacing: 0.04em; white-space: nowrap; }
  .wordmark span { display: block; font-size: 0.42em; letter-spacing: 0.12em; margin-top: 0.2em; }
  .envelope .wordmark { left: 22px; top: 30px; font-size: 30px; }
  .letterhead .wordmark { left: 28px; top: 30px; font-size: 30px; }
  .card-brand .wordmark { left: 28px; top: 62px; font-size: 54px; }

  .wave-band { position: absolute; border-radius: 50%;
    background: radial-gradient(ellipse at 55% 50%, rgba(240,197,106,0.55) 0%, rgba(200,145,46,0.35) 40%, rgba(200,145,46,0) 72%); }
  .envelope .wave-band { left: -40px; top: 80px; width: 620px; height: 180px; }
  .card-contact .wave-band { left: -30px; top: 70px; width: 540px; height: 140px; }
  .card-brand .wave-band { left: 120px; top: 120px; width: 400px; height: 150px; }
  .letterhead .wave-band { left: -40px; top: 70px; width: 690px; height: 200px; }

  .employee { position: absolute; z-index: 1; right: 30px; top: 24px; text-align: right; font-family: "Playfair Display", Georgia, serif; font-style: italic; font-weight: 700; }
  .employee-name { font-size: 42px; line-height: 1; }
  .employee-title { font-size: 22px; margin-top: 4px; margin-right: 20px; }

  .contact { position: absolute; z-index: 1; text-align: center; }
  .card-contact .contact { left: 150px; right: 20px; top: 140px; font-size: 11.5px; line-height: 1.25; }
  .letterhead .contact { left: 30px; right: 30px; top: 724px; font-size: 9px; line-height: 1.2; color: var(--ink-soft); }
  .tagline { font-weight: 600; color: var(--ink); margin-top: 2px; }
  .disclosure { font-size: 5.5px; color: var(--ink-soft); line-height: 1.25; }
  .card-contact .disclosure { position: absolute; z-index: 1; left: 12px; right: 12px; bottom: 8px; text-align: left; }
  .letterhead .disclosure { margin-top: 3px; }

  .rule { position: absolute; left: 0; right: 0; top: 714px; height: 2px; background: var(--gold); }
</style>
</head>
<body>
<main class="stationery">

  <section class="piece envelope" aria-label="Envelope">
    <div class="wave-band" role="img" aria-label="Flowing gold line wave pattern"></div>
    <div class="wordmark">Corvane<span>WEALTH MANAGEMENT</span></div>
  </section>

  <section class="piece card-contact" aria-label="Business card, contact side">
    <div class="wave-band" role="img" aria-label="Flowing gold line wave pattern"></div>
    <div class="employee">
      <p class="employee-name">Adrian Vale</p>
      <p class="employee-title">Manager</p>
    </div>
    <div class="contact">
      <p>adrian.vale@corvanewealth.com</p>
      <p>www.corvanewealth.com</p>
      <p>Main Office · Denver, CO 80202 · 555-014-2290</p>
      <p>Branch Office · Aspen, CO 81611 · 555-014-7731</p>
      <p class="tagline">Preferred Wealth Management for Select Individuals</p>
    </div>
    <p class="disclosure">Investment Advisory Services offered through Harrowgate Asset Partners LLC, a SEC Registered Investment Advisor. Corvane Wealth Management LLC is not affiliated with Harrowgate Asset Partners LLC.</p>
  </section>

  <section class="piece card-brand" aria-label="Business card, brand side">
    <div class="wave-band" role="img" aria-label="Flowing gold line wave pattern"></div>
    <div class="wordmark">Corvane<span>WEALTH MANAGEMENT</span></div>
  </section>

  <section class="piece letterhead" aria-label="Letterhead">
    <div class="wave-band" role="img" aria-label="Flowing gold line wave pattern"></div>
    <div class="wordmark">Corvane<span>WEALTH MANAGEMENT</span></div>
    <div class="rule"></div>
    <div class="contact">
      <p>adrian.vale@corvanewealth.com</p>
      <p>www.corvanewealth.com</p>
      <p>Main Office · Denver, CO 80202 · 555-014-2290</p>
      <p>Branch Office · Aspen, CO 81611 · 555-014-7731</p>
      <p class="tagline">Preferred Wealth Management for Select Individuals</p>
      <p class="disclosure">Investment Advisory Services offered through Harrowgate Asset Partners LLC, a SEC Registered Investment Advisor. Corvane Wealth Management LLC is not affiliated with Harrowgate Asset Partners LLC.</p>
    </div>
  </section>

</main>
</body>
</html>
```